Tarvin Group Business Card

Building Management company based in Sydney, Australia. We provide onsite management for commercial and residential buildings.
I would like a sophisticated minimalist design that indicates that we provide a high-end service. I would like a silver or metal look background or something similar.
The business card should have:
Name
Title
email
Office Phone
Mobile
Address
Website
The services that we provide should be prominent:
Building Management - Concierge - Caretaking - Cleaning

```html
<!DOCTYPE html>
<html lang="en">
<head>
<meta charset="utf-8">
<title>Tarvin Group Business Card</title>
<link rel="stylesheet" href="https://fonts.googleapis.com/css2?family=Arimo:wght@400;700&display=swap">
<style>
  :root {
    --stage-dark: #2e2e2e;
    --stage-light: #5a5a5a;
    --metal-dark: #a9a9a9;
    --metal-dark-edge: #9c9c9c;
    --metal-light: #c9c9c9;
    --metal-light-edge: #bdbdbd;
    --brand-blue: #1f78d1;
    --ink: #111111;
  }
  * { margin: 0; padding: 0; box-sizing: border-box; }
  html, body { width: 1200px; height: 900px; overflow: hidden; }
  body {
    background: radial-gradient(ellipse at 30% 10%, var(--stage-light), var(--stage-dark) 70%);
    font-family: "Arimo", Arial, sans-serif;
    position: relative;
  }
  .card {
    position: absolute;
    left: 335px;
    width: 530px;
    height: 303px;
    border-radius: 30px;
    overflow: hidden;
    box-shadow: 0 14px 30px rgba(0,0,0,.45);
  }
  .card--back { top: 110px; }
  .card--front { top: 480px; }
  .panel { position: absolute; top: 0; height: 100%; }
  .panel--dark {
    left: 0; width: 46%;
    background: repeating-linear-gradient(0deg, rgba(255,255,255,.05) 0 1px, transparent 1px 3px),
                linear-gradient(135deg, var(--metal-dark), var(--metal-dark-edge));
  }
  .panel--light {
    right: 0; width: 54%;
    background: repeating-linear-gradient(0deg, rgba(255,255,255,.06) 0 1px, transparent 1px 3px),
                linear-gradient(135deg, var(--metal-light), var(--metal-light-edge));
  }

  /* back card */
  .identity { position: absolute; right: 26px; top: 24px; text-align: right; }
  .identity__name { font-size: 24px; color: var(--ink); }
  .identity__name span { color: var(--brand-blue); }
  .identity__title { font-size: 15px; color: var(--ink); margin-top: 4px; }
  .website {
    position: absolute; left: 150px; top: 100px;
    color: var(--brand-blue); font-size: 21px; white-space: nowrap;
  }
  .contact-list {
    position: absolute; top: 178px;
    display: flex; flex-direction: column; gap: 12px;
  }
  .contact-list--phones { left: 26px; }
  .contact-list--mail { left: 268px; }
  .contact-line {
    display: flex; align-items: flex-start; gap: 8px;
    color: var(--brand-blue); font-size: 18px; line-height: 20px;
  }
  .contact-line svg { width: 20px; height: 20px; flex: none; fill: var(--brand-blue); }

  /* front card */
  .brand {
    position: absolute; left: 0; right: 0; top: 92px;
    display: flex; align-items: center; justify-content: center; gap: 16px;
    white-space: nowrap;
  }
  .brand__dot { width: 46px; height: 46px; border-radius: 50%; background: var(--brand-blue); flex: none; }
  .brand__name { font-size: 50px; font-weight: 700; color: var(--ink); letter-spacing: 1px; line-height: 1; }
  .services {
    position: absolute; left: 0; right: 0; top: 178px;
    display: flex; justify-content: center; gap: 10px;
    list-style: none;
    color: var(--brand-blue); font-size: 16px; font-weight: 700; white-space: nowrap;
  }
  .services li + li::before { content: "·"; margin-right: 10px; color: var(--ink); }
</style>
</head>
<body>

  <section class="card card--back" aria-label="Business card back">
    <div class="panel panel--dark"></div>
    <div class="panel panel--light"></div>

    <div class="identity">
      <p class="identity__name"><span>Your</span> Name</p>
      <p class="identity__title">Title</p>
    </div>

    <p class="website">www.yourwebsite.com</p>

    <div class="contact-list contact-list--phones">
      <div class="contact-line">
        <svg viewBox="0 0 24 24" aria-hidden="true"><rect x="1" y="1" width="22" height="22" rx="4"/><path d="M8 5c1 0 2 3 2 4s-1 1-1 2 2 4 4 4 1-1 2-1 4 1 4 2-2 3-4 3C9 19 5 13 5 8c0-2 2-3 3-3z" fill="#fff"/></svg>
        <span>012-3445-6789</span>
      </div>
      <div class="contact-line">
        <svg viewBox="0 0 24 24" aria-hidden="true"><path d="M2 9c0-3 4-5 10-5s10 2 10 5v2h-5V9H7v2H2z"/><path d="M5 13h14l2 8H3z"/></svg>
        <span>012-3445-6789</span>
      </div>
    </div>

    <div class="contact-list contact-list--mail">
      <div class="contact-line">
        <svg viewBox="0 0 24 24" aria-hidden="true"><rect x="1" y="4" width="22" height="16"/><path d="M2 5l10 8 10-8" stroke="#fff" stroke-width="2" fill="none"/></svg>
        <span>abcdef@yourmail.com</span>
      </div>
      <div class="contact-line">
        <svg viewBox="0 0 24 24" aria-hidden="true"><path d="M12 2L1 12h3v10h6v-6h4v6h6V12h3z"/></svg>
        <span>Your Address<br>Goes Here</span>
      </div>
    </div>
  </section>

  <section class="card card--front" aria-label="Business card front">
    <div class="panel panel--dark"></div>
    <div class="panel panel--light"></div>
    <div class="brand">
      <span class="brand__dot" aria-hidden="true"></span>
      <span class="brand__name">Tarvin Group</span>
    </div>
    <ul class="services">
      <li>Building Management</li>
      <li>Concierge</li>
      <li>Caretaking</li>
      <li>Cleaning</li>
    </ul>
  </section>

</body>
</html>
```